Business cards for a recruitment company
Marrowby Associates
Modern
Helena Marrowby
Managing Director
PO Box 48213 Corvel Harbour Plaza Dubai United Arab Emirates
lena@marrowbyassociates-mail.test
marrowbyassociates-mail.test
The business card needs to have my name, designation etc in both English and Arabic. Therefore, both languages will appear on the front of the card. The final design will illustrate how two different translations will appear on the front of the card. **The logo must also appear on the front of the card.
The back of the card will be plain white with just the logo as attached in the AI file. Perhaps the logo could be indented.

```html
<!DOCTYPE html>
<html lang="en">
<head>
<meta charset="utf-8">
<title>Marrowby Associates – Business Cards</title>
<link href="https://fonts.googleapis.com/css2?family=Open+Sans:wght@400;600&family=Noto+Naskh+Arabic:wght@500&display=swap" rel="stylesheet">
<style>
  :root {
    --backdrop: #d9d9d9;
    --card: #ffffff;
    --purple: #7d5c98;
    --ink: #2b2b2b;
    --grey: #6b6b6b;
    --shadow: rgba(0, 0, 0, 0.18);
  }
  html, body {
    margin: 0;
    padding: 0;
    width: 1200px;
    height: 902px;
    overflow: hidden;
    background: var(--backdrop);
    font-family: "Open Sans", Arial, sans-serif;
  }
  .stage { position: relative; width: 1200px; height: 902px; }
  .card {
    position: absolute;
    background: var(--card);
    box-shadow: 0 8px 22px var(--shadow);
  }
  .card-back { left: 120px; top: 50px; width: 620px; height: 354px; }
  .card-front { left: 460px; top: 470px; width: 700px; height: 400px; }

  .brand { display: flex; align-items: center; gap: 14px; }
  .brand-mark { width: 34px; height: 34px; background: var(--purple); flex: none; }
  .brand-name {
    color: var(--ink);
    font-weight: 400;
    letter-spacing: 0.12em;
    text-transform: uppercase;
    line-height: 1;
    white-space: nowrap;
  }
  .card-back .brand {
    position: absolute; left: 50%; top: 50%;
    transform: translate(-50%, -50%);
  }
  .card-back .brand-name { font-size: 30px; }
  .card-back .brand-mark { width: 46px; height: 46px; }

  .card-front .brand { position: absolute; left: 42px; top: 48px; }
  .card-front .brand-name { font-size: 25px; }
  .card-front .brand-mark { width: 40px; height: 40px; }

  .website {
    position: absolute; right: 40px; top: 212px;
    font-size: 13px; color: var(--purple); letter-spacing: 0.16em;
  }
  .identity { position: absolute; left: 42px; top: 202px; }
  .identity-en { font-size: 17px; color: var(--grey); margin: 0; }
  .person-name { color: var(--purple); font-weight: 600; }
  .divider { margin: 0 6px; color: var(--ink); }
  .identity-ar {
    font-family: "Noto Naskh Arabic", serif;
    font-size: 19px; color: var(--purple); margin: 4px 0 0;
    direction: rtl; text-align: left; unicode-bidi: plaintext;
  }
  .contacts {
    position: absolute; left: 42px; top: 276px;
    list-style: none; margin: 0; padding: 0;
    font-size: 12px; color: var(--grey); line-height: 19px;
  }
  .contacts li { display: flex; align-items: center; gap: 8px; }
  .contacts svg { width: 11px; height: 11px; flex: none; fill: var(--purple); }
  .contacts .indent { padding-left: 19px; }
</style>
</head>
<body>
<div class="stage">

  <section class="card card-back" aria-label="Card back">
    <div class="brand">
      <span class="brand-mark"></span>
      <span class="brand-name">Marrowby Associates</span>
    </div>
  </section>

  <section class="card card-front" aria-label="Card front">
    <div class="brand">
      <span class="brand-mark"></span>
      <span class="brand-name">Marrowby Associates</span>
    </div>

    <div class="website">www.marrowbyassociates-mail.test</div>

    <div class="identity">
      <p class="identity-en"><span class="person-name">Helena Marrowby</span><span class="divider">|</span>Managing Director</p>
      <p class="identity-ar">هيلينا ماروبي | المدير العام</p>
    </div>

    <ul class="contacts">
      <li>
        <svg viewBox="0 0 12 12"><path d="M2.5 0.5l2 2.5-1.2 1.2c0.8 1.6 2 2.8 3.5 3.5l1.2-1.2 2.5 2-1.5 2.5C4.5 10.5 1.5 7.5 0 2z"/></svg>
        +971-4-5550182
      </li>
      <li>
        <svg viewBox="0 0 12 12"><rect x="3" y="0" width="6" height="12" rx="1"/><rect x="4" y="1.5" width="4" height="7" fill="#fff"/></svg>
        +971-50-5550947
      </li>
      <li>
        <svg viewBox="0 0 12 12"><rect x="0" y="2" width="12" height="8"/><path d="M0.5 2.5L6 7l5.5-4.5" stroke="#fff" stroke-width="1" fill="none"/></svg>
        lena@marrowbyassociates-mail.test
      </li>
      <li>
        <svg viewBox="0 0 12 12"><path d="M6 0a4 4 0 0 1 4 4c0 3-4 8-4 8S2 7 2 4a4 4 0 0 1 4-4z"/><circle cx="6" cy="4" r="1.5" fill="#fff"/></svg>
        PO Box 48213, Corvel Harbour Plaza
      </li>
      <li class="indent">Dubai, United Arab Emirates</li>
    </ul>
  </section>

</div>
</body>
</html>
```